Bold Website Design for Fitness Trainer - No Coding

We are in need of a bold and unique website design for a personal fitness training company, www.TessaLorvel.com. We need DESIGN ONLY for three pages. These will be a homepage, a lead capture page, and one internal page with a sidebar. The design will be used for coding a wordpress theme, if that matters for the designer.

Tessa Lorvel Fitness Training
2738 E 19th St #415
Austin, TX 78705
512-607-4918
http://www.tessalorvel.com

Target Market(s)

18-45 year old male and females making 80k+ a year and looking to get stronger and in shape.

Industry/Entity Type

Fitness

Number of Pages Required

3 page

Font styles to use
Sans Serif

Requirements
Must have
• See attached design specs file.
Nice to have
Should not have
• Boxed layout.
• Dark Background.

```html
<!DOCTYPE html>
<html lang="en">
<head>
<meta charset="utf-8">
<title>Tessa Lorvel Fitness Training</title>
<link href="https://fonts.googleapis.com/css2?family=Open+Sans:wght@300;400;600;700&display=swap" rel="stylesheet">
<style>
:root{
  --blue:#1ba9e1;
  --blue-dark:#0f8fc4;
  --pink:#e8378f;
  --black:#111;
  --ink:#333;
  --muted:#666;
  --light:#f1f1f1;
  --line:#d6d6d6;
  --white:#fff;
}
*{box-sizing:border-box;margin:0;padding:0}
html,body{width:1200px;height:3035px;overflow:hidden}
body{font-family:"Open Sans",Arial,sans-serif;color:var(--ink);background:var(--white);font-size:13px}
.wrap{width:924px;margin:0 auto;position:relative}
a{color:inherit;text-decoration:none}
.icon{display:inline-block;vertical-align:middle}

/* top bar */
.topbar{height:46px;background:var(--blue);color:var(--white);font-size:13px}
.topbar .wrap{display:flex;align-items:center;height:46px;gap:28px}
.topbar span{display:flex;align-items:center;gap:7px}
.social{margin-left:auto;display:flex;gap:8px}
.social i{width:26px;height:26px;border-radius:50%;background:var(--white);opacity:.9;display:block}
.social.red i{background:#3b5998}

/* header */
.header{height:184px;background:radial-gradient(ellipse at 50% 50%,#fff7e6 0%,#fff 60%);display:flex;align-items:center;justify-content:center;gap:18px}
.brand-mark{width:120px;height:120px;border-radius:50%;background:#f3d21b}
.brand-name{font-size:58px;font-weight:700;color:#1b4f9c;letter-spacing:-1px}

/* nav */
.nav{height:46px;background:var(--black)}
.nav ul{list-style:none;display:flex;height:46px}
.nav li{color:var(--white);font-weight:700;font-size:16px;line-height:46px;padding:0 27px}
.nav li.active{background:var(--blue)}
.nav li.cta{background:var(--pink);margin-left:auto;padding:0 24px}

/* hero */
.hero{height:508px;position:relative;background:linear-gradient(110deg,#2b2b2b 0%,#8a8a8a 45%,#cfcfcf 70%,#7d7d7d 100%)}
.hero-arrow{position:absolute;top:236px;width:40px;height:36px;background:#222;display:flex;align-items:center;justify-content:center}
.hero-arrow.l{left:0}.hero-arrow.r{right:0}
.hero-tag{position:absolute;right:138px;top:376px;text-align:right;color:var(--white);font-size:37px;line-height:50px;font-weight:400;text-shadow:0 1px 3px rgba(0,0,0,.4)}

.getstarted{height:138px;background:linear-gradient(90deg,var(--blue-dark),var(--blue) 40%,#4fc1ee 100%)}
.getstarted .wrap{display:flex;align-items:center;height:138px;padding-left:22px}
.gs-text{color:var(--white);font-size:35px;line-height:52px;font-weight:400}
.gs-text b{font-size:50px;font-weight:700}
.btn-black{margin-left:auto;background:var(--black);color:var(--white);font-size:30px;font-weight:600;padding:10px 28px;letter-spacing:1px}

/* about */
.about{height:598px;background:var(--light);text-align:center;padding-top:52px}
h2.title{font-size:46px;font-weight:300;color:#222;letter-spacing:1px}
.lead{width:924px;margin:14px auto 0;font-size:12px;line-height:20px;color:var(--muted)}
.btn-outline{display:inline-block;border:1px solid var(--blue);color:var(--blue);font-size:12px;padding:7px 14px;background:var(--white)}
.about .btn-outline{margin-top:22px}
.services{display:flex;gap:32px;margin-top:46px}
.service{width:286px;background:var(--white);border:1px solid var(--line);text-align:left}
.service .ph{height:182px}
.service h3{color:var(--blue);font-size:17px;font-weight:400;padding:8px 12px 2px}
.service p{font-size:13px;color:var(--muted);padding:0 12px 18px;line-height:18px}

/* testimonials */
.testimonials{height:320px;text-align:center;padding-top:36px}
.testi-row{display:flex;justify-content:center;gap:66px;margin-top:44px;position:relative}
.testi{display:flex;gap:16px;text-align:left}
.avatar{width:104px;height:104px;border-radius:50%;margin-top:6px}
.quote{width:300px}
.bubble{border:1px solid var(--line);padding:10px 12px 10px 42px;font-size:12px;line-height:19px;color:var(--muted);position:relative;height:124px}
.bubble:before{content:"\201C";position:absolute;left:10px;top:-8px;font-size:48px;color:#9fd8f1;font-family:Georgia,serif}
.quote .who{font-size:12px;text-align:center;margin-top:12px}
.t-arrow{position:absolute;top:40px}
.t-arrow.l{left:100px}.t-arrow.r{right:100px}

/* social feeds */
.feeds{height:490px;background:var(--light);padding-top:30px}
.feeds .wrap{display:flex;justify-content:space-between;padding:0 20px}
.feed{width:412px}
.feed h2{display:flex;align-items:center;gap:14px;font-size:30px;font-weight:300;color:#222;margin-bottom:16px}
.feed h2 i{width:52px;height:52px;display:block;border-radius:6px}
.gridbox{border:2px solid #999;background:var(--white);padding:8px 10px;height:344px}
.gridbox p{font-size:15px;margin-bottom:16px}
.grid{display:grid;grid-template-columns:repeat(4,82px);gap:34px 16px;justify-content:center}
.grid i{height:66px;display:block;border:1px solid #bbb}
.fb{border:2px solid #bbb;background:var(--white);width:400px;height:350px;padding:10px 12px}
.fb-head{display:flex;gap:10px;border-bottom:1px solid #ddd;padding-bottom:10px}
.fb-head i{width:56px;height:56px;border-radius:50%;background:#f3d21b;border:2px solid #ccc;display:block}
.fb-head b{color:#3b5998;font-size:16px}
.fb-like{margin-top:6px;font-size:13px;display:flex;gap:8px;align-items:center}
.fb-like span{border:1px solid #ccc;background:#eee;padding:2px 8px;color:#999}
.fb-count{font-size:13px;font-weight:600;margin:10px 0 8px}
.faces{display:grid;grid-template-columns:repeat(5,66px);gap:8px 8px}
.faces div{font-size:11px;text-align:center;color:#555}
.faces i{display:block;height:66px;margin-bottom:3px}
.fb-foot{border-top:1px solid #ddd;margin-top:8px;padding-top:6px;font-size:11px;color:#555;display:flex;align-items:center;gap:6px}
.fb-foot i{width:14px;height:14px;background:#3b5998;display:block}

/* blog */
.blog{height:362px;text-align:center;padding-top:30px}
.posts{display:flex;justify-content:space-between;margin-top:28px;text-align:left}
.post{width:286px}
.post-head{display:flex;gap:10px;align-items:flex-start}
.post-head i{width:66px;height:66px;display:block;border:2px solid #ddd}
.post-head h4{font-size:18px;font-weight:400;color:#222}
.post-head small{font-size:12px;color:#555;display:block}
.post .by{font-size:10px;color:#777;text-align:right;border-bottom:1px solid #ddd;padding-bottom:4px;margin-top:4px}
.post p{font-size:12px;line-height:19px;color:var(--muted);margin:8px 0 14px}

/* pink band */
.band{height:110px;background:var(--pink);position:relative}
.band .wrap{display:flex;align-items:center;height:110px}
.band-get{position:absolute;left:138px;top:0;height:110px;width:290px;background:var(--white);clip-path:polygon(0 0,100% 0,86% 100%,0 100%);padding:6px 0 0 4px;color:var(--blue);font-size:36px;line-height:46px;font-weight:400}
.band-list{margin-left:280px;display:grid;grid-template-columns:170px 170px;gap:6px 12px;color:var(--white);font-size:14px}
.band-list span{display:flex;align-items:center;gap:7px}
.band-btn{margin-left:auto;background:var(--black);color:var(--white);text-align:center;padding:10px 22px;font-size:19px;font-weight:700;line-height:26px}
.band-btn small{display:block;font-size:15px;font-weight:400}

/* footer */
.footer{height:185px;background:var(--blue);color:var(--white)}
.footer .wrap{display:flex;padding-top:14px;gap:0}
.fcol h5{font-size:16px;font-weight:400;letter-spacing:.5px;border-bottom:1px solid rgba(255,255,255,.4);padding-bottom:6px;margin-bottom:10px}
.fcol{font-size:12px;line-height:20px}
.fcol.contact{width:220px}
.fcol.links{width:200px}
.fcol.stay{width:310px}
.fcol.connect{width:194px}
.crow{display:flex;gap:12px;align-items:flex-start;margin-bottom:10px}
.subscribe{display:flex;margin-top:12px}
.subscribe span{background:var(--white);color:#888;font-size:11px;padding:6px 10px;width:184px}
.subscribe b{background:var(--black);padding:6px 10px;font-size:13px;font-weight:600}
.fsoc{display:flex;gap:6px;margin:8px 0 10px}
.fsoc i{width:26px;height:26px;border-radius:50%;background:var(--white);display:block}
.fcircle{width:60px;height:60px;border-radius:50%;background:#1a3e6e;margin-left:44px}

.bottom{height:48px;background:var(--black);color:var(--white);font-size:12px}
.bottom .wrap{display:flex;align-items:center;height:48px}
.bottom .phone{margin-left:290px;font-size:17px;display:flex;gap:8px;align-items:center}
.bottom .legal{margin-left:auto;display:flex;gap:22px}
</style>
</head>
<body>

<div class="topbar">
  <div class="wrap">
    <span><svg class="icon" width="14" height="14" viewBox="0 0 14 14"><path d="M3 1l3 3-1.5 1.5a8 8 0 004 4L10 8l3 3-2 2C6 13 1 8 1 3z" fill="#fff"/></svg>123-456-7890</span>
    <span><svg class="icon" width="12" height="15" viewBox="0 0 12 15"><path d="M6 0a6 6 0 00-6 6c0 4 6 9 6 9s6-5 6-9a6 6 0 00-6-6zm0 8.5A2.5 2.5 0 116 3.5a2.5 2.5 0 010 5z" fill="#fff"/></svg>Training Locations</span>
    <span><svg class="icon" width="15" height="14" viewBox="0 0 15 14"><rect x="1" y="2" width="13" height="11" fill="none" stroke="#fff" stroke-width="1.5"/><line x1="1" y1="5" x2="14" y2="5" stroke="#fff" stroke-width="1.5"/></svg>Appointment Calendar</span>
    <div class="social"><i></i><i></i><i></i><i></i><i></i></div>
  </div>
</div>

<header class="header">
  <div class="brand-mark"></div>
  <div class="brand-name">Tessa Lorvel</div>
</header>

<nav class="nav">
  <div class="wrap">
    <ul>
      <li class="active">HOME</li>
      <li>PROGRAMS</li>
      <li>MEET YOUR TRAINER</li>
      <li>BLOG</li>
      <li>CONTACT ME</li>
      <li class="cta">FREE SESSION</li>
    </ul>
  </div>
</nav>

<section class="hero" role="img" aria-label="Black and white photo of a trainer spotting a client lifting dumbbells on a bench">
  <div class="hero-arrow l"><svg width="12" height="16" viewBox="0 0 12 16"><path d="M10 2L3 8l7 6" stroke="#fff" stroke-width="3" fill="none"/></svg></div>
  <div class="hero-arrow r"><svg width="12" height="16" viewBox="0 0 12 16"><path d="M2 2l7 6-7 6" stroke="#fff" stroke-width="3" fill="none"/></svg></div>
  <div class="hero-tag">Austin’s #1<br>Personal Trainer</div>
</section>

<section class="getstarted">
  <div class="wrap">
    <div class="gs-text">GET STARTED TODAY<br>YOUR FIRST SESSIONS IS <b>FREE</b></div>
    <a class="btn-black">SIGN UP NOW</a>
  </div>
</section>

<section class="about">
  <h2 class="title">ABOUT OUR SERVICES</h2>
  <p class="lead">Lorem ipsum dolor sit amet, consectetuer adipiscing elit, sed diam nonummy nibh euismod tincidunt ut laoreet dolore magna aliquam erat volutpat. Ut wisi enim ad minim veniam, quis nostrud exerci tation ullamcorper suscipit lobortis nisl ut aliquip ex ea commodo consequat. Duis autem vel eum iriure dolor in hendrerit in vulputate velit esse molestie consequat, vel illum dolore eu feugiat nulla facilisis at vero eros et accumsan et.</p>
  <a class="btn-outline">READ MORE</a>
  <div class="wrap services">
    <div class="service"><div class="ph" role="img" aria-label="Trainer assisting a client with dumbbells" style="background:linear-gradient(135deg,#3a3a3a,#9a9a9a)"></div><h3>1 ON 1 PERSONAL TRAINING</h3><p>Lorem ipsum dolor sit amet, consectetuer adipiscing elit, sed diam nonummy</p></div>
    <div class="service"><div class="ph" role="img" aria-label="Woman in a suit working on a laptop beside dumbbells" style="background:linear-gradient(135deg,#e9e6e1,#b7aea4)"></div><h3>ONLINE COACHING</h3><p>Lorem ipsum dolor sit amet, consectetuer adipiscing elit, sed diam nonummy</p></div>
    <div class="service"><div class="ph" role="img" aria-label="Muscular arm lifting a dumbbell" style="background:linear-gradient(135deg,#2e2e2e,#b07b5a)"></div><h3>STRENGTH PROGRAMMING</h3><p>Lorem ipsum dolor sit amet, consectetuer adipiscing elit, sed diam nonummy</p></div>
  </div>
</section>

<section class="testimonials">
  <h2 class="title">TESTIMONIALS</h2>
  <div class="testi-row">
    <svg class="t-arrow l" width="20" height="40" viewBox="0 0 20 40"><path d="M18 2L3 20l15 18" stroke="#555" stroke-width="2" fill="none"/></svg>
    <div class="testi">
      <div class="avatar" role="img" aria-label="Client portrait" style="background:linear-gradient(#bfc7cf,#6d7d8c)"></div>
      <div class="quote"><div class="bubble">Lorem ipsum dolor sit amet, consectetuer adipiscing elit, sed diam nonummy nibh erofdf euismod tincidunt ut laoreet dolore magna aliquam erat volutpat. Ut wisi enim ad minim veniam, quis nostrud.</div><div class="who">Lorem Ipsum</div></div>
    </div>
    <div class="testi">
      <div class="avatar" role="img" aria-label="Client portrait" style="background:linear-gradient(#333,#8a6a55)"></div>
      <div class="quote"><div class="bubble">Lorem ipsum dolor sit amet, consectetuer adipiscing elit, sed diam nonummy nibh erofdf euismod tincidunt ut laoreet dolore magna aliquam erat volutpat. Ut wisi enim ad minim veniam, quis nostrud.</div><div class="who">Lorem Ipsum</div></div>
    </div>
    <svg class="t-arrow r" width="20" height="40" viewBox="0 0 20 40"><path d="M2 2l15 18L2 38" stroke="#555" stroke-width="2" fill="none"/></svg>
  </div>
</section>

<section class="feeds">
  <div class="wrap">
    <div class="feed">
      <h2><i style="background:#8a6f55"></i>SNAPGRID</h2>
      <div class="gridbox">
        <p>Currently photos trending on snapgrid</p>
        <div class="grid" role="img" aria-label="Grid of twelve recent training photos">
          <i style="background:#d9a0b3"></i><i style="background:#555"></i><i style="background:#c9c4bd"></i><i style="background:#b56a6a"></i>
          <i style="background:#8d8d8d"></i><i style="background:#c27d7d"></i><i style="background:#333"></i><i style="background:#999"></i>
          <i style="background:#bdb6ad"></i><i style="background:#5a5a5a"></i><i style="background:#777"></i><i style="background:#d49aae"></i>
        </div>
      </div>
    </div>
    <div class="feed">
      <h2><i style="background:#3b5998"></i>FIND US ON FRIENDWALL</h2>
      <div class="fb">
        <div class="fb-head"><i></i><div><b>Tessa Lorvel Fitness Training</b> on <b>Friendwall</b><div class="fb-like"><span>Like</span>You like this.</div></div></div>
        <div class="fb-count">516 people like Tessa Lorvel Fitness Training.</div>
        <div class="faces" role="img" aria-label="Profile photos of page followers">
          <div><i style="background:#c9a27e"></i>Avery</div><div><i style="background:#a5786a"></i>Dana</div><div><i style="background:#d8b8a0"></i>Kelsey</div><div><i style="background:#b28a70"></i>Rory</div><div><i style="background:#c99a86"></i>Tamsin</div>
          <div><i style="background:#6d6d6d"></i></div><div><i style="background:#8a7a6a"></i></div><div><i style="background:#9a5a4a"></i></div><div><i style="background:#b69a8a"></i></div><div><i style="background:#a08070"></i></div>
        </div>
        <div class="fb-foot"><i></i>Friendwall social plugin</div>
      </div>
    </div>
  </div>
</section>

<section class="blog">
  <h2 class="title">FROM THE BLOG</h2>
  <div class="wrap posts">
    <div class="post"><div class="post-head"><i role="img" aria-label="Blog thumbnail" style="background:#c9c4bd"></i><div><h4>Lorem Ispum</h4><small>13th Jun, 2015</small></div></div><div class="by">posted by Tessa Lorvel Fitness Training</div><p>Lorem ipsum dolor sit amet, consectetuer adipiscing elit, sed diam nonummy nibh euismod tincidunt ut laoreet dolore magna aliquam erat volutpat.</p><a class="btn-outline">READ MORE</a></div>
    <div class="post"><div class="post-head"><i role="img" aria-label="Blog thumbnail" style="background:#555"></i><div><h4>Lorem Ispum</h4><small>12th Jun, 2015</small></div></div><div class="by">posted by Tessa Lorvel Fitness Training</div><p>Lorem ipsum dolor sit amet, consectetuer adipiscing elit, sed diam nonummy nibh euismod tincidunt ut laoreet dolore magna aliquam erat volutpat.</p><a class="btn-outline">READ MORE</a></div>
    <div class="post"><div class="post-head"><i role="img" aria-label="Blog thumbnail" style="background:#d49aae"></i><div><h4>Lorem Ispum</h4><small>12th Jun, 2015</small></div></div><div class="by">posted by Tessa Lorvel Fitness Training</div><p>Lorem ipsum dolor sit amet, consectetuer adipiscing elit, sed diam nonummy nibh euismod tincidunt ut laoreet dolore magna aliquam erat volutpat.</p><a class="btn-outline">READ MORE</a></div>
  </div>
</section>

<section class="band">
  <div class="band-get">GET<br>Started Today</div>
  <div class="wrap">
    <div class="band-list">
      <span><svg width="14" height="14" viewBox="0 0 14 14"><circle cx="7" cy="7" r="7" fill="#fff"/><path d="M3.5 7l2.5 2.5 4.5-5" stroke="#e8378f" stroke-width="2" fill="none"/></svg>Personal Training</span>
      <span><svg width="14" height="14" viewBox="0 0 14 14"><circle cx="7" cy="7" r="7" fill="#fff"/><path d="M3.5 7l2.5 2.5 4.5-5" stroke="#e8378f" stroke-width="2" fill="none"/></svg>Strength Training</span>
      <span><svg width="14" height="14" viewBox="0 0 14 14"><circle cx="7" cy="7" r="7" fill="#fff"/><path d="M3.5 7l2.5 2.5 4.5-5" stroke="#e8378f" stroke-width="2" fill="none"/></svg>General Fitness</span>
      <span><svg width="14" height="14" viewBox="0 0 14 14"><circle cx="7" cy="7" r="7" fill="#fff"/><path d="M3.5 7l2.5 2.5 4.5-5" stroke="#e8378f" stroke-width="2" fill="none"/></svg>Power Lifting</span>
      <span><svg width="14" height="14" viewBox="0 0 14 14"><circle cx="7" cy="7" r="7" fill="#fff"/><path d="M3.5 7l2.5 2.5 4.5-5" stroke="#e8378f" stroke-width="2" fill="none"/></svg>Weight Loss</span>
      <span><svg width="14" height="14" viewBox="0 0 14 14"><circle cx="7" cy="7" r="7" fill="#fff"/><path d="M3.5 7l2.5 2.5 4.5-5" stroke="#e8378f" stroke-width="2" fill="none"/></svg>Olympic Lifting</span>
    </div>
    <a class="band-btn">GET STARTED TODAY<small>YOUR FIRST SESSIONS IS FREE</small></a>
  </div>
</section>

<footer class="footer">
  <div class="wrap">
    <div class="fcol contact">
      <h5>CONTACT DETAILS</h5>
      <div class="crow"><svg width="12" height="15" viewBox="0 0 12 15"><path d="M6 0a6 6 0 00-6 6c0 4 6 9 6 9s6-5 6-9a6 6 0 00-6-6zm0 8.5A2.5 2.5 0 116 3.5a2.5 2.5 0 010 5z" fill="#fff"/></svg><span style="line-height:16px">Street Name City Name<br>State Zipcode</span></div>
      <div class="crow"><svg width="14" height="14" viewBox="0 0 14 14"><path d="M3 1l3 3-1.5 1.5a8 8 0 004 4L10 8l3 3-2 2C6 13 1 8 1 3z" fill="#fff"/></svg>123-456-7890</div>
      <div class="crow"><svg width="14" height="11" viewBox="0 0 14 11"><rect width="14" height="11" fill="#fff"/><path d="M0 0l7 6 7-6" stroke="#1ba9e1" fill="none"/></svg>inquiry@tessalorvel.com</div>
    </div>
    <div class="fcol links">
      <h5>QUICK LINKS</h5>
      <div style="line-height:20px">HOME<br>PROGRAMS<br>MEET YOUR TRAINER<br>BLOG<br>CONTACT ME</div>
    </div>
    <div class="fcol stay">
      <h5>STAY IN TOUCH</h5>
      <p style="line-height:18px">Lorem ipsum dolor sit amet, consectetuer adipiscing elit, sed diam nonummy nibh euismod tincidunt ut laoreet dolore.</p>
      <div class="subscribe"><span>Enter your email here</span><b>Subscribe</b></div>
    </div>
    <div class="fcol connect">
      <h5>CONNECT WITH US</h5>
      <div class="fsoc"><i></i><i></i><i></i><i></i><i></i></div>
      <div class="fcircle"></div>
    </div>
  </div>
</footer>

<div class="bottom">
  <div class="wrap">
    <span>© 2015 TessaLorvel. All Rights Reserved</span>
    <span class="phone"><svg width="14" height="14" viewBox="0 0 14 14"><path d="M3 1l3 3-1.5 1.5a8 8 0 004 4L10 8l3 3-2 2C6 13 1 8 1 3z" fill="#fff"/></svg>123-456-7890</span>
    <span class="legal"><span>Term of Use</span><span>Privacy Policy</span></span>
  </div>
</div>

</body>
</html>
```